New business card design

I need original, modern, business looking but dzen (minimalistic) looking design.
Also refer to websit qvtrenda.ru

Text is

Зорин Виктор, PMP
Партнер

Моб. +7 (915) 460 1897
info@qvtrenda.ru
Москва, Россия, 117358, ул. Берёзовая 27/2
=====================

Zorin Viktor, PMP
Partner

Mob. +7 (915) 460 1897
info@qvtrenda.ru
Moscow, Russia,117358, Beryozovaya 27/2

```html
<!DOCTYPE html>
<html lang="en">
<head>
<meta charset="utf-8">
<title>QVTrenda — Business Card</title>
<link href="https://fonts.googleapis.com/css2?family=Roboto:wght@300;400;700&display=swap" rel="stylesheet">
<style>
  :root {
    --bg: #2b2b2d;
    --blue-light: #35aee6;
    --blue-mid: #1f9ad9;
    --blue-deep: #0f7fc4;
    --white: #ffffff;
    --name-blue: #1c8fd0;
    --logo-grey: #2f3a45;
    --card-w: 700px;
    --card-h: 389px;
  }
  * { margin: 0; padding: 0; box-sizing: border-box; }
  html, body {
    width: 1200px; height: 900px; overflow: hidden;
    background: var(--bg);
    font-family: "Roboto", Arial, sans-serif;
  }
  .canvas {
    width: 1200px; height: 900px;
    display: flex; flex-direction: column;
    align-items: center; justify-content: center; gap: 40px;
  }
  .card {
    width: var(--card-w); height: var(--card-h);
    position: relative; overflow: hidden;
  }

  /* Back side */
  .card-back {
    background: radial-gradient(ellipse at 70% 40%, var(--blue-light) 0%, var(--blue-mid) 55%, var(--blue-deep) 100%);
    display: flex; align-items: center; justify-content: center;
  }
  .card-back .brand {
    display: flex; align-items: center; gap: 22px;
  }
  .card-back .brand-mark {
    width: 58px; height: 58px; background: rgba(255,255,255,0.35);
  }
  .card-back .brand-name {
    font-weight: 300; font-size: 76px; color: var(--white); letter-spacing: 1px;
  }

  /* Front side */
  .card-front {
    background: radial-gradient(ellipse at 75% 35%, var(--blue-light) 0%, var(--blue-mid) 60%, var(--blue-deep) 100%);
  }
  .front-panel {
    position: absolute; left: 0; top: 0; width: 316px; height: 100%;
  }
  .front-panel svg { position: absolute; inset: 0; }
  .front-identity {
    position: absolute; left: 0; top: 0; width: 300px; height: 100%;
    display: flex; flex-direction: column; align-items: center;
  }
  .front-identity .brand {
    margin-top: 96px; display: flex; align-items: center; gap: 14px;
  }
  .front-identity .brand-mark {
    width: 40px; height: 40px; background: var(--blue-mid);
  }
  .front-identity .brand-name {
    font-weight: 300; font-size: 40px; color: var(--logo-grey);
  }
  .person { margin-top: 78px; text-align: center; }
  .person-name {
    font-weight: 700; font-size: 19px; color: var(--name-blue); letter-spacing: 0.5px;
  }
  .person-role {
    font-weight: 400; font-size: 18px; color: var(--name-blue); margin-top: 2px;
  }

  .contacts {
    position: absolute; left: 356px; top: 100px;
    list-style: none; color: var(--white);
  }
  .contacts li {
    display: flex; align-items: flex-start; gap: 14px;
    font-weight: 300; font-size: 17px; line-height: 1.2; margin-bottom: 16px;
  }
  .contacts svg { flex: none; width: 18px; height: 18px; margin-top: 1px; }
</style>
</head>
<body>
<main class="canvas">

  <section class="card card-back" aria-label="Card back">
    <div class="brand">
      <span class="brand-mark"></span>
      <span class="brand-name">QVTrenda</span>
    </div>
  </section>

  <section class="card card-front" aria-label="Card front">
    <div class="front-panel">
      <svg viewBox="0 0 316 389" width="316" height="389" aria-hidden="true">
        <path d="M0 0 H276 Q300 0 300 24 V22 Q300 40 316 48 V341 Q300 349 300 367 V389 H0 Z" fill="#ffffff"/>
      </svg>
    </div>
    <div class="front-identity">
      <div class="brand">
        <span class="brand-mark"></span>
        <span class="brand-name">QVTrenda</span>
      </div>
      <div class="person">
        <p class="person-name">Zorin Viktor, PMP</p>
        <p class="person-role">Partner</p>
      </div>
    </div>

    <ul class="contacts">
      <li>
        <svg viewBox="0 0 24 24" aria-hidden="true"><path fill="#fff" d="M6.6 10.8a15 15 0 0 0 6.6 6.6l2.2-2.2a1 1 0 0 1 1-.25 11.4 11.4 0 0 0 3.6.57 1 1 0 0 1 1 1V20a1 1 0 0 1-1 1A17 17 0 0 1 3 4a1 1 0 0 1 1-1h3.5a1 1 0 0 1 1 1c0 1.25.2 2.45.57 3.6a1 1 0 0 1-.25 1z"/></svg>
        <span>+7 (915) 460 1897</span>
      </li>
      <li>
        <svg viewBox="0 0 24 24" aria-hidden="true"><rect x="2" y="5" width="20" height="14" rx="1" fill="none" stroke="#fff" stroke-width="2"/><path d="M2 6l10 7 10-7" fill="none" stroke="#fff" stroke-width="2"/></svg>
        <span>info@qvtrenda.ru</span>
      </li>
      <li>
        <svg viewBox="0 0 24 24" aria-hidden="true"><path fill="#fff" d="M12 2a7 7 0 0 0-7 7c0 5 7 13 7 13s7-8 7-13a7 7 0 0 0-7-7zm0 9.5A2.5 2.5 0 1 1 12 6.5a2.5 2.5 0 0 1 0 5z"/></svg>
        <span>Moscow, Russia,117358,<br>Beryozovaya 27/2</span>
      </li>
    </ul>
  </section>

</main>
</body>
</html>
```